IT Consulting Business needs a web design

We need a web design for an IT Consulting company called "Vorenix". We want to replace the existing web site (www.vorenix-example.com) with a new design. Our services are IT Consulting, IT Training, IT Outsourcing.
We would like to see designs that communicate "Trusted IT Advisor" with modern & bold design.

We would like to see the design of 2 pages:
1. Home page (www.vorenix-example.com)
2. The detail page (http://www.vorenix-example.com/index_files/consulting.htm)

Industry/Entity Type

Business

```html
<!DOCTYPE html>
<html lang="en">
<head>
<meta charset="utf-8">
<title>Vorenix – IT Consulting</title>
<link rel="stylesheet" href="https://fonts.googleapis.com/css2?family=Open+Sans:ital,wght@0,400;0,600;1,400;1,600&family=Arimo:wght@400;700&display=swap">
<style>
:root{
  --page-bg:#e9e9e9;
  --sheet:#ffffff;
  --band:#f1f1f1;
  --blue:#1a5bb5;
  --blue-dark:#0f4ea3;
  --red:#e0161b;
  --ink:#555555;
  --ink-soft:#777777;
  --rule:#dddddd;
  --nav-top:#a9a9a9;
  --nav-bottom:#8c8c8c;
}
*{margin:0;padding:0;box-sizing:border-box}
html,body{width:1200px;height:1121px;overflow:hidden}
body{background:var(--page-bg);font-family:"Arimo",Arial,sans-serif;color:var(--ink);position:relative}
h2,h3{font-weight:400}
.sheet{position:absolute;left:123px;top:0;width:962px;height:1121px;background:var(--sheet)}
.abs{position:absolute}

.contact{top:10px;font-size:11px;color:var(--ink-soft);display:flex;align-items:center;gap:6px}
.contact svg{fill:#999}
.contact-phone{left:803px}
.contact-mail{left:913px}

.logo{left:187px;top:20px;font-weight:700;font-size:37px;color:var(--blue);letter-spacing:1.5px}

.nav{left:463px;top:32px;width:571px;height:26px;display:flex;background:linear-gradient(var(--nav-top),var(--nav-bottom));box-shadow:0 2px 3px rgba(0,0,0,.2)}
.nav a{flex:1;color:#fff;text-decoration:none;font-size:11px;display:flex;align-items:center;justify-content:center}
.nav a.active{background:linear-gradient(#2a6fd0,var(--blue-dark));flex:0 0 65px}
.header-rule{left:176px;top:74px;width:858px;height:1px;background:#eeeeee}

.hero{left:176px;top:88px;width:858px;height:272px;background:linear-gradient(90deg,#dedede 0%,#eceff2 30%,#4a4f5e 48%,#e9edf0 62%,#d4dbe3 85%,#eef1f3 100%);box-shadow:0 12px 14px -8px rgba(0,0,0,.35)}
.hero-title{left:643px;top:164px;width:363px;display:flex;align-items:center;gap:4px;font-family:"Open Sans",sans-serif;font-style:italic;font-size:23px;color:#444;white-space:nowrap}
.hero-title i{flex:1;height:1px;background:#666}
.hero-btn{left:740px;top:213px;width:140px;height:25px;background:var(--red);color:#fff;font-family:"Open Sans",sans-serif;font-weight:600;font-size:14px;display:flex;align-items:center;justify-content:center;border-radius:2px}

.section-title{top:394px;left:406px;width:360px;display:flex;align-items:center;gap:14px;font-family:"Open Sans",sans-serif;font-style:italic;font-size:22px;color:#555;white-space:nowrap}
.section-title i{flex:1;height:1px;background:#aaa}

.value{top:445px;width:190px;text-align:center}
.value svg{display:block;margin:0 auto;fill:none;stroke:var(--blue);stroke-width:3.2}
.value h3{margin-top:8px;font-family:"Open Sans",sans-serif;font-style:italic;font-size:20px;color:#555;white-space:nowrap}
.value p{margin-top:2px;font-size:9px;line-height:12px;color:#666}

.band{left:123px;top:563px;width:962px;height:346px;background:var(--band)}
.tagline{left:176px;top:582px;font-family:"Open Sans",sans-serif;font-style:italic;font-size:20.3px;color:#555;white-space:nowrap}
.tagline em{color:var(--blue)}

.card{top:633px;width:272px;height:234px;background:#fff;box-shadow:0 12px 12px -8px rgba(0,0,0,.3)}
.card-img{height:141px}
.card-head{margin:12px 22px 0;display:flex;justify-content:space-between;align-items:center;padding-bottom:6px;border-bottom:1px solid var(--rule)}
.card-head h3{font-family:"Open Sans",sans-serif;font-style:italic;font-size:20px;color:#666}
.card p{margin:10px 22px 0;font-size:9px;line-height:12px;color:#666}
.img-consulting{background:linear-gradient(120deg,#4e8fd1,#9fc6ea 55%,#dcebf8)}
.img-training{background:linear-gradient(120deg,#6a7a8e,#b9c9d8 50%,#5d86b3)}
.img-outsourcing{background:linear-gradient(160deg,#dfe8f8,#9db4e8 60%,#c6d5f2)}

.about-title{left:180px;top:932px;font-family:"Open Sans",sans-serif;font-style:italic;font-size:16.5px;color:var(--blue)}
.about-text{left:176px;top:961px;width:560px;font-size:9.2px;line-height:12.5px;color:#444}
.about-text strong{display:block;margin-top:2px}
.svc-list{display:grid;grid-template-columns:258px 1fr;list-style:none}
.divider{left:764px;top:923px;width:1px;height:102px;background:var(--rule)}
.stay-title{left:802px;top:932px;font-family:"Open Sans",sans-serif;font-style:italic;font-size:16px;color:var(--blue)}
.social{top:968px;width:22px;height:22px;border-radius:50%;background:#555}

.footer-rule{left:176px;top:1043px;width:858px;height:1px;background:var(--rule)}
.footer-nav{left:178px;top:1066px;display:flex;font-size:9.5px;color:#444}
.footer-nav a{color:#444;text-decoration:none}
.footer-logo{left:938px;top:1064px;font-weight:700;font-size:22px;color:var(--blue);letter-spacing:1.2px}
</style>
</head>
<body>
<div class="sheet"></div>

<div class="abs contact contact-phone">
  <svg width="12" height="10" viewBox="0 0 12 10"><path d="M1 3c0-2 10-2 10 0v1H8V3H4v1H1zM3 5h6l2 4H1z"/></svg>02-555-0147
</div>
<div class="abs contact contact-mail">
  <svg width="12" height="9" viewBox="0 0 12 9"><rect x="0.5" y="0.5" width="11" height="8" fill="none" stroke="#999"/><path d="M1 1l5 4 5-4" fill="none" stroke="#999"/></svg>info@vorenix-example.com
</div>

<div class="abs logo">Vorenix</div>

<nav class="abs nav">
  <a class="active" href="#">Home</a>
  <a href="#">Services</a>
  <a href="#">Our Expertise</a>
  <a href="#">Jobs</a>
  <a href="#">About Us</a>
  <a href="#">Contact Us</a>
</nav>
<div class="abs header-rule"></div>

<div class="abs hero" role="img" aria-label="Photo of a consultant presenting at a flip chart to a seated team"></div>
<div class="abs hero-title"><i></i>Your Most Trusted IT Advisor<i></i></div>
<div class="abs hero-btn">know more</div>

<h2 class="abs section-title"><i></i>Our Values &amp; Services<i></i></h2>

<div class="abs value" style="left:139px">
  <svg width="44" height="30" viewBox="0 0 44 30"><path d="M4 8h9l16 14h9M4 22h9l16-14h9"/><path d="M33 3l6 5-6 5M33 17l6 5-6 5"/></svg>
  <h3>Fast</h3><p>Lorem ipsum dolor sit amet<br>consectetur adipiscing</p>
</div>
<div class="abs value" style="left:318px">
  <svg width="44" height="30" viewBox="0 0 44 30"><path d="M26 5H8v22h24v-8"/><path d="M14 21c2-8 8-11 18-11M28 5l6 5-6 5"/></svg>
  <h3>High Quality</h3><p>Lorem ipsum dolor sit amet<br>consectetur adipiscing</p>
</div>
<div class="abs value" style="left:502px">
  <svg width="44" height="30" viewBox="0 0 44 30"><path d="M10 4l24 24M34 4L10 28"/><path d="M6 2l8 0 0 6M38 2l-6 0 0 6"/></svg>
  <h3>Services</h3><p>Lorem ipsum dolor sit amet<br>consectetur adipiscing</p>
</div>
<div class="abs value" style="left:695px">
  <svg width="44" height="30" viewBox="0 0 44 30"><path d="M8 6h4M8 15h4M8 24h4M17 6h20M17 15h20M17 24h20"/></svg>
  <h3>Customised</h3><p>Lorem ipsum dolor sit amet<br>consectetur adipiscing</p>
</div>
<div class="abs value" style="left:878px">
  <svg width="44" height="30" viewBox="0 0 44 30"><rect x="8" y="3" width="20" height="16"/><rect x="15" y="10" width="22" height="17"/></svg>
  <h3>Customer focus</h3><p>Lorem ipsum dolor sit amet<br>consectetur adipiscing</p>
</div>

<div class="abs band"></div>
<p class="abs tagline">Experienced, certified professionals provide <em>IT consulting</em> by industry recommended practices.</p>

<article class="abs card" style="left:174px">
  <div class="card-img img-consulting" role="img" aria-label="Photo of a businessman reaching out for a handshake"></div>
  <div class="card-head"><h3>IT Consulting</h3>
    <svg width="20" height="20" viewBox="0 0 20 20"><circle cx="10" cy="10" r="9" fill="#b5b5b5"/><path d="M8 6l5 4-5 4z" fill="#fff"/></svg></div>
  <p>Lorem ipsum dolor sit amet consec adipiscing elitvi vamus ut neque augtortor velit bibenn.</p>
</article>
<article class="abs card" style="left:467px">
  <div class="card-img img-training" role="img" aria-label="Photo of a team in a training meeting around a table"></div>
  <div class="card-head"><h3>IT Training</h3>
    <svg width="20" height="20" viewBox="0 0 20 20"><circle cx="10" cy="10" r="9" fill="#b5b5b5"/><rect x="5" y="10" width="2" height="4" fill="#fff"/><rect x="9" y="7" width="2" height="7" fill="#fff"/><rect x="13" y="10" width="2" height="4" fill="#fff"/></svg></div>
  <p>Lorem ipsum dolor sit amet consec adipiscing elitvi vamus ut neque augtortor velit bibenn.</p>
</article>
<article class="abs card" style="left:761px">
  <div class="card-img img-outsourcing" role="img" aria-label="Illustration of a world map above a row of business people"></div>
  <div class="card-head"><h3>IT Outsourcing</h3>
    <svg width="20" height="20" viewBox="0 0 20 20"><circle cx="10" cy="10" r="9" fill="#b5b5b5"/><circle cx="10" cy="10" r="5.5" fill="none" stroke="#fff"/><path d="M4.5 10h11M10 4.5v11" stroke="#fff"/></svg></div>
  <p>Lorem ipsum dolor sit amet consec adipiscing elitvi vamus ut neque augtortor velit bibenn.</p>
</article>

<h2 class="abs about-title">About our Consulting Services</h2>
<div class="abs about-text">
  <p>Our experienced, certified professionals provides IT consulting using industry recommended practices. We are specialized in Corvane Business Productivity Platform using Corvane TeamVault Technologies and Business Intelligence Platform.</p>
  <strong>Some of our services are:</strong>
  <ul class="svc-list">
    <li>· Strategic technology consulting and advice</li>
    <li>· Business technology improvements</li>
    <li>· Business technology reviews, audits, and studies</li>
    <li>· Solution architecture &amp; implementation for applications of all sizes</li>
  </ul>
</div>
<div class="abs divider"></div>
<h2 class="abs stay-title">Stay Connected</h2>
<span class="abs social" style="left:802px"></span>
<span class="abs social" style="left:835px"></span>
<span class="abs social" style="left:869px"></span>
<span class="abs social" style="left:902px"></span>

<div class="abs footer-rule"></div>
<nav class="abs footer-nav">
  <a href="#" style="width:73px">Home</a>
  <a href="#" style="width:77px">Services</a>
  <a href="#" style="width:106px">Our Expertise</a>
  <a href="#" style="width:64px">Jobs</a>
  <a href="#" style="width:79px">About Us</a>
  <a href="#">Contact Us</a>
</nav>
<div class="abs footer-logo">Vorenix</div>
</body>
</html>
```